Realty Group Needs Classy, Contemporary Letterhead Design

We need a letterhead design for a new realty company located in NY, USA. We buy investment properties to rehabilitate and or keep in our rental portfolio.

```html
<!DOCTYPE html>
<html lang="en">
<head>
<meta charset="utf-8">
<title>Meridian Realty Group – Letterhead</title>
<link href="https://fonts.googleapis.com/css2?family=Arimo:wght@400;700&family=Montserrat:wght@500;700&display=swap" rel="stylesheet">
<style>
  :root{
    --backdrop:#7d5aaa;
    --paper:#f4f4f5;
    --brand:#4f2585;
    --ink:#1e1e1e;
    --ink-soft:#3a3a3a;
    --rule:#6a6a6a;
    --ghost:rgba(79,37,133,0.05);
    --placeholder:#d9d9dc;
  }
  *{margin:0;padding:0;box-sizing:border-box}
  html,body{width:1200px;height:1200px;overflow:hidden}
  body{background:var(--backdrop);position:relative;font-family:"Arimo",Arial,sans-serif;color:var(--ink)}
  .letterhead{position:absolute;left:205px;top:40px;width:790px;height:1120px;background:var(--paper);overflow:hidden}
  .header-band{position:absolute;left:0;top:147px;width:86px;height:47px;background:var(--brand)}
  .brand{position:absolute;left:99px;top:148px;width:228px;text-align:center}
  .brand-name{font-family:"Arimo",Arial,sans-serif;font-weight:700;font-size:32px;letter-spacing:-0.5px;color:var(--brand);line-height:40px}
  .brand-sub{display:flex;align-items:center;gap:8px;font-family:"Montserrat",sans-serif;font-weight:500;font-size:11px;letter-spacing:1px;color:var(--ink-soft)}
  .brand-sub::before,.brand-sub::after{content:"";flex:1;height:1px;background:var(--ink-soft)}
  .tagline-art{position:absolute;left:554px;top:144px;width:190px;height:83px;background:linear-gradient(135deg,var(--placeholder),#e7e7ea);border-radius:4px}
  .meta{position:absolute;left:100px;top:343px;font-size:16px}
  .meta .subject{margin-top:10px;font-weight:700;text-decoration:underline}
  .body-copy{position:absolute;left:100px;top:412px;width:590px;font-size:10.6px;line-height:18px;color:var(--ink-soft)}
  .body-copy p+p{margin-top:18px}
  .signature-art{position:absolute;left:101px;top:790px;width:196px;height:52px;background:linear-gradient(135deg,var(--placeholder),#e7e7ea);border-radius:4px}
  .signature-rule{position:absolute;left:101px;top:843px;width:196px;height:1px;background:var(--rule)}
  .signer{position:absolute;left:106px;top:852px;font-size:13px;line-height:16px}
  .signer strong{display:block;font-weight:700}
  .footer-rule{position:absolute;left:85px;top:959px;width:3px;height:161px;background:var(--brand)}
  .footer-brand{position:absolute;left:99px;top:962px;width:152px;text-align:center}
  .footer-brand .brand-name{font-size:22px;line-height:28px;letter-spacing:-0.3px}
  .footer-brand .brand-sub{font-size:7px;gap:5px;letter-spacing:0.6px}
  .contact{position:absolute;left:99px;top:1023px;font-family:"Montserrat",sans-serif;color:var(--brand)}
  .contact .address{font-weight:700;font-size:10.5px;line-height:11px;text-transform:uppercase}
  .contact .phone{margin-top:14px;font-weight:700;font-size:10.5px}
  .contact .web{margin-top:10px;font-size:8px;font-weight:500;color:var(--ink-soft)}
  .contact .web b{color:var(--brand)}
  .ghost-name{position:absolute;left:90px;top:1040px;font-family:"Arimo",Arial,sans-serif;font-weight:700;font-size:108px;letter-spacing:-2px;color:var(--ghost);white-space:nowrap;line-height:1}
  .corner-block{position:absolute;right:0;bottom:0;width:44px;height:44px;background:var(--brand)}
</style>
</head>
<body>
  <main class="letterhead">
    <div class="ghost-name" aria-hidden="true">MERIDIAN</div>
    <div class="header-band"></div>
    <div class="brand">
      <div class="brand-name">MERIDIAN</div>
      <div class="brand-sub">Realty Group, LLC</div>
    </div>
    <div class="tagline-art" role="img" aria-label="Hand-lettered tagline reading lorem ipsum dolor"></div>

    <section class="meta">
      <p>Date: 23 November 2013</p>
      <p class="subject">RE: Lorem ipsum dolor sit amet</p>
    </section>

    <section class="body-copy">
      <p>Lorem ipsum dolor sit amet, consectetuer adipiscing elit, sed diam nonummy nibh euismod tincidunt ut laoreet dolore magna aliquam erat volutpat. Ut wisi enim ad minim veniam, quis nostrud exerci tation ullamcorper suscipit lobortis nisl ut aliquip ex ea commodo consequat.</p>
      <p>Lorem ipsum dolor sit amet, consectetuer adipiscing elit, sed diam nonummy nibh euismod tincidunt ut laoreet dolore magna aliquam erat volutpat. Ut wisi enim ad minim veniam, quis nostrud exerci tation ullamcorper suscipit lobortis nisl ut aliquip ex ea commodo consequat. Lorem ipsum dolor sit amet, consectetuer adipiscing elit, sed diam nonummy nibh euismod tincidunt ut laoreet dolore magna aliquam erat volutpat.</p>
      <p>Lorem ipsum dolor sit amet, consectetuer adipiscing elit, sed diam nonummy nibh euismod tincidunt ut laoreet dolore magna aliquam erat volutpat. Ut wisi enim ad minim veniam, quis nostrud exerci tation ullamcorper suscipit lobortis nisl ut aliquip ex ea commodo consequat.Lorem ipsum dolor sit amet, consectetuer adipiscing elit, sed diam nonummy nibh euismod tincidunt ut laoreet dolore magna aliquam erat volutpat. Ut wisi enim ad minim veniam, quis nostrud exerci tation ullamcorper suscipit lobortis nisl ut aliquip ex ea commodo consequat.</p>
      <p>Lorem ipsum dolor sit amet, consectetuer adipiscing elit, sed diam nonummy nibh euismod tincidunt ut laoreet dolore magna aliquam erat volutpat.</p>
    </section>

    <div class="signature-art" role="img" aria-label="Handwritten signature of John Doe"></div>
    <div class="signature-rule"></div>
    <div class="signer"><strong>JOHN DOE</strong>Senior manager</div>

    <div class="footer-rule"></div>
    <div class="footer-brand">
      <div class="brand-name">MERIDIAN</div>
      <div class="brand-sub">Realty Group, LLC</div>
    </div>
    <address class="contact" style="font-style:normal">
      <div class="address">218 Harbor Street STE-4<br>Hudson Bay, NY 10521</div>
      <div class="phone">555 204 18 00</div>
      <div class="web">www.<b>meridianrealtygroup</b>.com</div>
    </address>
    <div class="corner-block"></div>
  </main>
</body>
</html>
```